Sumvane financial services stationery design

We need business stationery designed with letterheads, business cards, with compliments and envelope for a business that offers tax and accounting services

Designs look the same

Target Market(s)

Small to medium businesses, individuals, Self managed superfunds

Industry/Entity Type

Business

Font styles to use
Serif
Other font styles liked:
• Atlanta

Colors
32a6d6
3277b5

Requirements
Must have
• Logo incorporated with all my stationery
• professional
Should not have
• Lots of colours
• Busy

```html
<!DOCTYPE html>
<html lang="en">
<head>
<meta charset="utf-8">
<title>Sumvane Financial Services – Business Card</title>
<link rel="stylesheet" href="https://fonts.googleapis.com/css2?family=Cinzel:wght@500&family=Roboto:wght@400&display=swap">
<style>
  :root {
    --bg: #e9eaec;
    --card-blue: #1265a5;
    --brand-blue: #3277b5;
    --brand-sky: #32a6d6;
    --paper: #f7f7f7;
    --ink: #2b2b2b;
    --white: #ffffff;
  }
  * { margin: 0; padding: 0; box-sizing: border-box; }
  html, body { width: 1200px; height: 726px; overflow: hidden; background: var(--bg); }
  .canvas {
    position: relative; width: 1200px; height: 726px;
    display: flex; align-items: center; justify-content: center; gap: 48px;
  }
  .card {
    position: relative; width: 520px; height: 297px; overflow: hidden;
    box-shadow: 0 6px 18px rgba(0,0,0,0.12);
  }
  .card--front { background: var(--card-blue); display: flex; align-items: center; justify-content: center; }
  .card--back { background: var(--paper); }

  .brand { display: flex; align-items: center; gap: 14px; }
  .brand__square { width: 46px; height: 46px; border-radius: 6px; }
  .brand__name {
    font-family: "Cinzel", serif; font-weight: 500; letter-spacing: 2px; line-height: 1;
  }
  .card--front .brand__square { background: var(--white); }
  .card--front .brand__name { color: var(--white); font-size: 44px; }
  .card--back .brand { position: absolute; right: 34px; top: 112px; }
  .card--back .brand__square { width: 34px; height: 34px; background: var(--brand-blue); border-radius: 4px; }
  .card--back .brand__name { color: var(--ink); font-size: 28px; }

  .holder { position: absolute; left: 44px; top: 38px; }
  .holder__name {
    font-family: "Cinzel", serif; font-weight: 500; font-size: 22px; color: var(--card-blue); letter-spacing: 1px;
  }
  .holder__role { font-family: "Roboto", sans-serif; font-size: 13px; color: var(--ink); margin-top: 2px; }
  .tab {
    position: absolute; left: -12px; top: 50px; width: 24px; height: 34px;
    border-radius: 0 17px 17px 0; background: var(--brand-blue);
  }

  .contact {
    position: absolute; left: 44px; bottom: 30px;
    font-family: "Roboto", sans-serif; font-size: 14px; color: var(--ink); line-height: 1.35;
  }
  .contact__address { margin-bottom: 4px; }
  .contact__row { display: flex; align-items: center; gap: 10px; }
  .contact__icon { width: 13px; height: 13px; flex: none; }
</style>
</head>
<body>
<main class="canvas">
  <section class="card card--front" aria-label="Business card front">
    <div class="brand">
      <span class="brand__square"></span>
      <span class="brand__name">SUMVANE</span>
    </div>
  </section>

  <section class="card card--back" aria-label="Business card back">
    <span class="tab"></span>
    <div class="holder">
      <p class="holder__name">DANIEL HARROW</p>
      <p class="holder__role">Managing Partner</p>
    </div>
    <div class="brand">
      <span class="brand__square"></span>
      <span class="brand__name">SUMVANE</span>
    </div>
    <div class="contact">
      <p class="contact__address">123, Street Number, Your City<br>Your Town, Country 123456</p>
      <p class="contact__row">
        <svg class="contact__icon" viewBox="0 0 16 16" aria-hidden="true"><path fill="#3277b5" d="M3 1h3l1.5 4-2 1.5a9 9 0 0 0 4 4L11 8.5l4 1.5v3a2 2 0 0 1-2 2A12 12 0 0 1 1 3a2 2 0 0 1 2-2z"/></svg>
        (012) 555 0148
      </p>
      <p class="contact__row">
        <svg class="contact__icon" viewBox="0 0 16 16" aria-hidden="true"><rect x="1" y="3" width="14" height="10" rx="1" fill="#3277b5"/><path d="M1.5 3.5 8 9l6.5-5.5" stroke="#fff" stroke-width="1.3" fill="none"/></svg>
        daniel@sumvanefinancial.com
      </p>
      <p class="contact__row">
        <svg class="contact__icon" viewBox="0 0 16 16" aria-hidden="true"><circle cx="8" cy="8" r="7" fill="#3277b5"/><path d="M1 8h14M8 1c3 3 3 11 0 14M8 1c-3 3-3 11 0 14" stroke="#fff" stroke-width="1" fill="none"/></svg>
        www.sumvanefinancial.com
      </p>
    </div>
  </section>
</main>
</body>
</html>
```